Webbanner-Design für Konferenz- und Messeformat
Zielgruppe
VOLMARKTIS - forum for smart commerce || Das virtuelle Konferenz- und Messeformat, wenn es um das Thema Digitalisierung geht.
Mit diesem Format adressieren wir Aussteller, Referenten und Besucher, welche sich um die Digitalisierung von Kundenprojekten kümmern. Dies mit Produkten, Lösungen aber auch Beratungsleistungen. Die Zielgruppe unserer Besucher sind die Unternehmen, welche nach geeigneten Lösungen suchen und Ihr Business digitaler gestalten möchten, somit auch entsprechende Projekte auf der Agenda haben.
Daher sind unsere Hauptthemen der Veranstaltung: Industrie 4.0, digital future, digital Workplace, IT Infrastruktur. Eine detaillierte thematische Gliederung finden Sie anbei.
Das besondere an der VOLMARKTIS ist, dass wir kein Konferenz- und Messeformat im „klassischen“ physischen Sinne sind. Unser Format ist voll digitalisiert und wird virtuell durchgeführt. Dies hat für die Aussteller die wesentlichen Vorteile:
- Kostengünstige Teilnahme als Referent und Aussteller
- Keine Reiseaufwendungen
- Weniger Standpersonal
- Größere Reichweite für Besucher mit geringerem Budget
- Größere Skalierbarkeit in Bezug auf Besuchergruppen
- Statistische Erfassung des Besucherverhalten und somit die Erzeugung von vorqualifizierten Leads
- Möglichkeit neue Zielgruppen zu erreichen, welche immer mehr von den traditionellen Messeformaten fernbleiben
-- Insbesondere durch die flexible Teilnahme an den Veranstaltungstagen und in der OnDemand Phase
Die hier zu erstellenden Banner sollen zwei Zwecke erfüllen. Zum einen wird es im Mai ein Mailing durch unseren Partner plovo geben, wo wir die Veranstaltung gegenüber potentiellen Ausstellern, Referenten und Sponsoren bewerben. Dieser Banner soll jedoch ebenso auf der zugehörigen plovo Eventseite als Header dienen. In selbigen Zusammenhang ist das Icon für die plovo Event Seiten zu gestalten.
Daher benötigen wir ein Design für den Header im..
Aufgabenstellung
Das sind die Bannergrößen für das Mailing
Megabanner desktop: 600 x 250 px
Megabanner mobil: 400 x 300 px
Das ist die größe für den Header / Banner auf der plovo Event Seite
Abmessungen: mind. 984 x 311 Pixel (B x H)
Das ist die größe für das Icon auf der plovo Event Seite
Quadratisches Bild mit mind. 256 x 256 Pixel (B x H), max. 3200 x 3200 Pixel
Dateiformat: JPG, PNG, BMP oder GIF + Quelldatei
Größe für den Upload: max. 5 MB
Farbmodus: RGB (kein CMYK etc.)
Bitte geben Sie bitte die zusätzlichen Kosten für evtl. benötigte Stockmedien an.

```html
<!DOCTYPE html>
<html lang="de">
<head>
<meta charset="utf-8">
<title>VOLMARKTIS – Webbanner</title>
<link rel="stylesheet" href="https://fonts.googleapis.com/css2?family=Open+Sans:wght@400;600;700&family=Raleway:wght@400;500;600&display=swap">
<style>
  :root {
    --navy: #0a2352;
    --navy-deep: #061a40;
    --blue: #0b63ad;
    --blue-light: #1b8fd6;
    --accent: #2aa7e8;
    --white: #ffffff;
    --red: #e2474a;
    --red-dark: #b8262c;
    --paper: #ffffff;
  }
  * { margin: 0; padding: 0; box-sizing: border-box; }
  html, body { width: 1200px; height: 1193px; overflow: hidden; background: var(--paper); }
  body { position: relative; font-family: "Open Sans", Arial, sans-serif; color: var(--white); }

  .panel {
    position: absolute;
    overflow: hidden;
    background:
      radial-gradient(ellipse at 75% 105%, var(--blue-light) 0%, rgba(27,143,214,0) 55%),
      linear-gradient(160deg, var(--navy-deep) 0%, var(--navy) 40%, var(--blue) 100%);
  }

  /* Header */
  .header { left: 0; top: 0; width: 1200px; height: 383px; }
  .header-photo {
    position: absolute; left: 0; top: 0; width: 481px; height: 383px;
    clip-path: polygon(0 0, 100% 0, 57.6% 100%, 0 100%);
    background: linear-gradient(170deg, #9fb4cf 0%, #c98e72 45%, #8a4b3c 75%, #d9c6bd 100%);
  }
  .header-bands { position: absolute; left: 0; top: 0; }
  .header .brand { left: 567px; top: 104px; }
  .header .rule { left: 568px; top: 190px; width: 545px; }
  .header .tagline { left: 568px; top: 199px; font-size: 22px; }
  .header .cta { left: 327px; top: 76px; width: 178px; height: 178px; font-size: 22px; }

  .icon-tile {
    position: absolute; left: 123px; top: 259px; width: 158px; height: 158px;
    border: 1px solid var(--white);
    background: linear-gradient(150deg, var(--navy) 0%, var(--blue) 100%);
    display: flex; align-items: center; justify-content: center;
  }
  .icon-tile .icon-name {
    font-family: "Raleway", Arial, sans-serif; font-weight: 600; font-size: 21px; letter-spacing: 0.5px;
    color: var(--white);
  }

  /* Shared pieces */
  .brand {
    position: absolute; display: flex; align-items: center; gap: 14px;
    font-family: "Raleway", Arial, sans-serif; font-weight: 600; color: var(--white);
    font-size: 78px; line-height: 1; letter-spacing: 1px; white-space: nowrap;
  }
  .brand-mark { width: 22px; height: 22px; background: var(--accent); flex: none; }
  .tagline {
    position: absolute; font-family: "Raleway", Arial, sans-serif; font-weight: 500;
    white-space: nowrap; letter-spacing: 0;
  }
  .rule {
    position: absolute; height: 2px;
    background: linear-gradient(90deg, rgba(255,255,255,0) 0%, rgba(255,255,255,0.85) 50%, rgba(255,255,255,0) 100%);
  }
  .event-label, .event-date { position: absolute; font-weight: 600; font-size: 16px; white-space: nowrap; }
  .benefits {
    position: absolute; list-style: none; font-size: 16px;
    font-family: "Raleway", Arial, sans-serif; font-weight: 500;
  }
  .benefits li { display: flex; align-items: center; gap: 8px; white-space: nowrap; }
  .benefits svg { flex: none; }

  .cta {
    position: absolute; border-radius: 50%;
    background: radial-gradient(circle at 40% 35%, #f06a68 0%, var(--red) 45%, var(--red-dark) 100%);
    box-shadow: 0 4px 12px rgba(0,0,0,0.35);
    display: flex; align-items: center; justify-content: center;
    font-family: "Open Sans", Arial, sans-serif; text-align: center; line-height: 1.05;
  }
  .cta > .cta-text { display: block; transform: rotate(-20deg); }
  .cta .cta-lead, .cta .cta-main { display: block; }
  .cta .cta-lead { font-weight: 400; }
  .cta .cta-main { font-weight: 700; }

  /* Desktop megabanner 600x250 */
  .mega-desktop { left: 122px; top: 439px; width: 740px; height: 308px; }
  .mega-desktop .brand { left: 100px; top: 20px; font-size: 70px; }
  .mega-desktop .tagline { left: 100px; top: 98px; font-size: 19px; }
  .mega-desktop .rule { left: 100px; top: 127px; width: 500px; }
  .mega-desktop .event-label { left: 125px; top: 136px; }
  .mega-desktop .event-date { right: 128px; top: 136px; }
  .mega-desktop .benefits { left: 122px; top: 181px; }
  .mega-desktop .benefits li { height: 26.5px; }
  .mega-desktop .cta { left: 488px; top: 171px; width: 124px; height: 124px; font-size: 16px; }

  /* Mobile megabanner 400x300 */
  .mega-mobile { left: 122px; top: 779px; width: 493px; height: 370px; }
  .mega-mobile .brand { left: 18px; top: 28px; font-size: 62px; gap: 10px; }
  .mega-mobile .brand-mark { width: 18px; height: 18px; }
  .mega-mobile .tagline { left: 19px; top: 102px; font-size: 17px; }
  .mega-mobile .rule { left: 19px; top: 131px; width: 455px; }
  .mega-mobile .event-label { left: 20px; top: 145px; font-size: 15px; }
  .mega-mobile .event-date { right: 22px; top: 145px; font-size: 15px; }
  .mega-mobile .benefits { left: 20px; top: 220px; font-size: 15px; }
  .mega-mobile .benefits li { height: 24.6px; }
  .mega-mobile .cta { left: 333px; top: 201px; width: 138px; height: 138px; font-size: 17px; }
</style>
</head>
<body>

<section class="panel header" aria-label="Header Eventseite">
  <div class="header-photo" role="img" aria-label="Foto: Publikum im Konferenzsaal vor Bühne und Leinwand"></div>
  <svg class="header-bands" width="1200" height="383" viewBox="0 0 1200 383" aria-hidden="true">
    <polygon points="481,0 500,0 296,383 277,383" fill="#ffffff" opacity="0.9"/>
    <polygon points="505,0 540,0 336,383 301,383" fill="#ffffff" opacity="0.18"/>
  </svg>
  <div class="brand"><span class="brand-mark"></span>VOLMARKTIS</div>
  <div class="rule"></div>
  <div class="tagline">FORUM FOR SMART COMMERCE - LIFE IS DIGITAL</div>
  <div class="cta"><span class="cta-text"><span class="cta-lead">JETZT</span><span class="cta-main">AUSSTELLER<br>WERDEN</span></span></div>
</section>

<div class="icon-tile" aria-label="Icon Eventseite"><span class="icon-name">VOLMARKTIS</span></div>

<section class="panel mega-desktop" aria-label="Megabanner desktop">
  <div class="brand"><span class="brand-mark"></span>VOLMARKTIS</div>
  <div class="tagline">FORUM FOR SMART COMMERCE - LIFE IS DIGITAL</div>
  <div class="rule"></div>
  <div class="event-label">Veranstaltungstermin</div>
  <div class="event-date">05. – 07. November 2019</div>
  <ul class="benefits">
    <li><svg width="12" height="10" viewBox="0 0 12 10"><path d="M1 1l4 4-4 4M6 1l4 4-4 4" fill="none" stroke="#2aa7e8" stroke-width="1.6"/></svg>Kostengünstige Teilnahme</li>
    <li><svg width="12" height="10" viewBox="0 0 12 10"><path d="M1 1l4 4-4 4M6 1l4 4-4 4" fill="none" stroke="#2aa7e8" stroke-width="1.6"/></svg>Keine Reiseaufwendungen</li>
    <li><svg width="12" height="10" viewBox="0 0 12 10"><path d="M1 1l4 4-4 4M6 1l4 4-4 4" fill="none" stroke="#2aa7e8" stroke-width="1.6"/></svg>Größere Reichweite</li>
    <li><svg width="12" height="10" viewBox="0 0 12 10"><path d="M1 1l4 4-4 4M6 1l4 4-4 4" fill="none" stroke="#2aa7e8" stroke-width="1.6"/></svg>Größere Skalierbarkeit</li>
  </ul>
  <div class="cta"><span class="cta-text"><span class="cta-lead">JETZT</span><span class="cta-main">AUSSTELLER<br>WERDEN</span></span></div>
</section>

<section class="panel mega-mobile" aria-label="Megabanner mobil">
  <div class="brand"><span class="brand-mark"></span>VOLMARKTIS</div>
  <div class="tagline">FORUM FOR SMART COMMERCE - LIFE IS DIGITAL</div>
  <div class="rule"></div>
  <div class="event-label">Veranstaltungstermin</div>
  <div class="event-date">05. – 07. November 2019</div>
  <ul class="benefits">
    <li><svg width="12" height="10" viewBox="0 0 12 10"><path d="M1 1l4 4-4 4M6 1l4 4-4 4" fill="none" stroke="#2aa7e8" stroke-width="1.6"/></svg>Kostengünstige Teilnahme</li>
    <li><svg width="12" height="10" viewBox="0 0 12 10"><path d="M1 1l4 4-4 4M6 1l4 4-4 4" fill="none" stroke="#2aa7e8" stroke-width="1.6"/></svg>Keine Reiseaufwendungen</li>
    <li><svg width="12" height="10" viewBox="0 0 12 10"><path d="M1 1l4 4-4 4M6 1l4 4-4 4" fill="none" stroke="#2aa7e8" stroke-width="1.6"/></svg>Größere Reichweite</li>
    <li><svg width="12" height="10" viewBox="0 0 12 10"><path d="M1 1l4 4-4 4M6 1l4 4-4 4" fill="none" stroke="#2aa7e8" stroke-width="1.6"/></svg>Größere Skalierbarkeit</li>
  </ul>
  <div class="cta"><span class="cta-text"><span class="cta-lead">JETZT</span><span class="cta-main">AUSSTELLER<br>WERDEN</span></span></div>
</section>

</body>
</html>
```